Hack my website! Blue Harbor needs a site

We hack stuff. No joke, that is what we do, but we are the good guys!

We do security consulting, specifically offensive security. The technical term is "Penetration Testing", but you probably know it as "hacking". Companies hire us to break in before the bad guys do. (I have a very cool job :) ).

I need a web site to describe our offerings and connect with clients.

I've included my business card and logo so you can understand what I'm looking for on the website and the color scheme.

Tag line:
Offensive Services from Offensive Minds

Target Market(s)

Medium to large businesses

Industry/Entity Type

Computer Security

Coding

Coded - Design and coding required

Number of Pages Required

2 page

Font styles to use
Sans Serif

Colors

Designer to choose colors to be used in the design.

Requirements
Must have
• Flat, clean, professional look
Nice to have
• Bonus for bootstrap. See the uploaded logo for the current colors. I'd really like this to look decent on a phone too.
Should not have
• 1. Black background
• 2. The business card is to show the colors and theme so far. Please, do NOT just slam that into the middle of the site since it doesn't make sense. It feels odd that I have to say that, but I've received multiple submissions where people have done this.

```html
<!DOCTYPE html>
<html lang="en">
<head>
<meta charset="utf-8">
<title>Blue Harbor – Offensive Security</title>
<link rel="stylesheet" href="https://fonts.googleapis.com/css2?family=Roboto+Condensed:wght@400;700&family=Roboto:ital,wght@0,400;0,500;0,700;1,400&display=swap">
<style>
:root{
  --red:#d51f27;
  --ink:#1d1d1d;
  --text:#444;
  --muted:#777;
  --light:#ececec;
  --panel:#bdbdbd;
  --footer:#1f1f1f;
  --white:#fff;
}
*{box-sizing:border-box;margin:0;padding:0}
html,body{width:1200px;height:3429px;overflow:hidden}
body{position:relative;background:var(--white);font-family:"Roboto",Arial,sans-serif;color:var(--text)}
.abs{position:absolute}
.cond{font-family:"Roboto Condensed","Arial Narrow",sans-serif}

/* nav */
.site-nav{left:0;top:0;width:1200px;height:46px;background:var(--white)}
.brand{left:160px;top:11px;display:flex;align-items:center;gap:8px;font-family:"Roboto Condensed",sans-serif;font-weight:700;font-size:22px;letter-spacing:2px;color:var(--red)}
.brand-mark{width:18px;height:18px;background:var(--red)}
.nav-links{right:160px;top:17px;display:flex;gap:26px;font-size:12px;font-weight:500;color:var(--ink)}

/* hero */
.hero{left:0;top:46px;width:1200px;height:560px;background:radial-gradient(ellipse at 35% 30%,#8d8d8d 0%,#4a4a4a 45%,#1c1c1c 100%)}
.hero-line{left:50%;transform:translateX(-50%);font-family:"Roboto Condensed",sans-serif;font-weight:700;text-transform:uppercase;white-space:nowrap}
.hero-line.one{top:327px;background:var(--white);color:var(--ink);font-size:44px;padding:0 14px;line-height:52px}
.hero-line.two{top:384px;background:var(--red);color:var(--white);font-size:36px;padding:0 14px;line-height:46px}

/* welcome */
.section-title{left:0;width:1200px;text-align:center;font-family:"Roboto Condensed",sans-serif;font-weight:700;font-size:34px;color:var(--ink);text-transform:uppercase}
.section-title .accent{color:var(--red)}
.title-rule{height:1px;background:#cfcfcf}
.welcome-copy{left:160px;top:700px;width:880px;text-align:center;font-size:11.5px;line-height:17px;color:var(--muted)}
.service-card{top:811px;width:279px;height:204px}
.service-card .photo{width:100%;height:168px}
.service-card .label{height:36px;background:var(--red);color:var(--white);font-weight:700;font-size:15px;text-align:center;line-height:36px;text-transform:uppercase}

/* consulting band */
.consult{left:0;top:1064px;width:1200px;height:296px;background:linear-gradient(90deg,#6b6b6b,#9a9a9a 50%,#5f5f5f)}
.consult-kicker{top:1106px;font-size:40px;color:var(--white)}
.consult-head{top:1150px;font-size:96px;letter-spacing:-2px;color:var(--white);line-height:100px}
.consult-sub{top:1248px;left:0;width:1200px;text-align:center;font-size:14px;letter-spacing:.5px;color:#eee;text-transform:uppercase}
.btn-ghost{left:535px;top:1289px;width:130px;height:35px;border:2px solid var(--white);color:var(--white);font-size:12px;font-weight:700;text-align:center;line-height:31px}

.red-band{left:0;top:1360px;width:1200px;height:80px;background:var(--red);text-align:center;color:var(--white)}
.red-band h2{font-family:"Roboto Condensed",sans-serif;font-weight:700;font-size:30px;margin-top:14px}
.red-band p{font-size:10px;font-weight:500;text-transform:uppercase;margin-top:2px}
.band-notch{left:570px;top:1439px}

/* offerings */
.offer-photo{left:160px;top:1548px;width:407px;height:317px;background:linear-gradient(135deg,#4b5c72,#a8b6c4 55%,#e3e7ec)}
.offer-panel{left:567px;top:1518px;width:473px;height:377px;background:var(--light);padding:38px 28px 0 30px}
.offer-kicker{font-family:"Roboto Condensed",sans-serif;font-weight:700;font-size:20px;color:var(--red)}
.offer-title{font-family:"Roboto Condensed",sans-serif;font-weight:700;font-size:24px;color:var(--ink);margin-left:52px;line-height:26px}
.offer-copy{margin-top:18px;font-size:11.5px;line-height:18.6px;color:var(--text)}
.btn-outline{display:inline-block;margin-top:26px;width:105px;height:31px;border:1.5px solid var(--ink);font-size:11px;font-weight:700;text-align:center;line-height:28px;color:var(--ink)}

/* clients */
.clients-kicker{top:1933px;font-size:16px;font-weight:700}
.clients-title{top:1950px;font-size:40px}
.testimonials{left:0;top:2021px;width:1200px;height:309px;background:linear-gradient(90deg,#e4e4e4,#c9c9c9 15%,#ededed 30%,#c4c4c4 70%,#ededed 85%,#d6d6d6)}
.quote-card{left:402px;top:2021px;width:398px;height:309px;background:var(--white)}
.avatar{left:556px;top:2068px;width:90px;height:90px;border-radius:50%;background:linear-gradient(#b9b9b9,#6c6c6c);border:4px solid #e6e6e6}
.quote{left:430px;top:2178px;width:340px;text-align:center;font-style:italic;font-weight:500;font-size:11.5px;line-height:17px;color:var(--ink)}
.quote-mark{font-family:Georgia,serif;font-size:34px;font-weight:700;color:var(--ink);line-height:1}
.quote-name{left:0;width:1200px;top:2227px;text-align:center;font-size:13px;color:var(--red);font-weight:500}

/* blog */
.blog-rule{left:580px;top:2405px;width:40px;height:3px;background:var(--red)}
.blog-hero{left:160px;top:2448px;width:427px;height:293px;background:linear-gradient(120deg,#f3d8a6,#d49a63 45%,#6e5b52)}
.date{width:48px;height:46px;background:var(--red);color:var(--white);text-align:center;font-weight:700;line-height:15px;padding-top:8px;font-size:14px}
.date small{display:block;font-size:11px}
.post-thumb{left:610px;width:128px;height:122px}
.post-body{left:757px;width:283px}
.post-body h3{font-size:13px;font-weight:700;color:var(--ink)}
.post-meta{font-size:10px;color:var(--muted);margin-top:6px}
.post-meta b{color:var(--ink);font-weight:500}
.post-excerpt{font-size:10.5px;line-height:15px;color:var(--muted);margin-top:8px}
.post-actions{display:flex;align-items:center;margin-top:10px;font-size:10px;color:var(--ink)}
.post-actions .btn-outline{margin:0 40px 0 0;width:86px;height:28px;line-height:25px;font-size:10px}
.post-actions span{display:flex;align-items:center;gap:5px;margin-right:32px}
.post-divider{left:610px;top:2594px;width:430px;height:1px;background:#e0e0e0}

/* cta + newsletter + footer */
.cta{left:0;top:2826px;width:1200px;height:265px;background:var(--red)}
.cta-title{left:160px;top:2880px;font-family:"Roboto Condensed",sans-serif;font-weight:700;font-size:30px;color:var(--white)}
.cta-copy{left:170px;top:2917px;font-size:12px;font-weight:500;color:var(--white)}
.btn-dark{left:780px;top:2881px;width:260px;height:46px;background:var(--ink);color:var(--white);font-weight:700;font-size:15px;display:flex;align-items:center;justify-content:center;gap:10px}
.footer{left:0;top:3091px;width:1200px;height:338px;background:var(--footer)}
.newsletter{left:160px;top:3001px;width:880px;height:177px;background:var(--panel);text-align:center}
.newsletter h2{font-family:"Roboto Condensed",sans-serif;font-weight:700;font-size:28px;color:var(--ink);margin-top:22px}
.newsletter p{font-size:12px;color:var(--ink);margin-top:4px}
.subscribe{display:flex;justify-content:center;margin-top:16px}
.subscribe .field{width:352px;height:40px;background:var(--white);text-align:left;padding-left:14px;font-size:11px;color:#999;line-height:40px}
.subscribe .go{width:110px;height:40px;background:var(--ink);color:var(--white);font-size:14px;line-height:40px}
.join{left:0;top:3196px;width:1200px;text-align:center;font-size:37px;font-weight:500;color:var(--white)}
.socials{left:487px;top:3263px;display:flex;gap:12px}
.socials span{width:34px;height:34px;border-radius:50%;border:1.5px solid #bbb}
.footer-links{left:0;top:3357px;width:1200px;text-align:center;font-size:10.5px;color:#bbb;word-spacing:2px}
.footer-links i{font-style:normal;margin:0 12px}
.copyright{left:0;top:3385px;width:1200px;text-align:center;font-size:10px;color:#888}
</style>
</head>
<body>

<header class="abs site-nav">
  <div class="abs brand"><span class="brand-mark"></span>BLUE HARBOR</div>
  <nav class="abs nav-links"><span>HOME</span><span>ABOUT US</span><span>OUR SERVICES</span><span>CONTACT US</span></nav>
</header>

<section>
  <div class="abs hero" role="img" aria-label="Monochrome photo of a hand touching a glowing padlock icon linked to network devices"></div>
  <div class="abs hero-line one">Offensive Solutions From</div>
  <div class="abs hero-line two">Offensive Minds</div>
</section>

<section>
  <div class="abs title-rule" style="left:160px;top:666px;width:290px"></div>
  <div class="abs title-rule" style="left:750px;top:666px;width:290px"></div>
  <h1 class="abs section-title" style="top:644px">Welcome to <span class="accent">Blue Harbor</span></h1>
  <p class="abs welcome-copy">Lorem Ipsum is simply dummy text of the printing and typesetting industry. Lorem Ipsum has been the industry's standard dummy text ever since the 1500s, when an unknown printer took a galley of type and scrambled it to make a type specimen book. It has survived not only five centuries, but also the leap into electronic typesetting, remaining essentially unchanged. It was popularised in the 1960s with the release of Typeset sheets containing Lorem Ipsum passages, and more recently with desktop publishing software like Folio Layout including versions of Lorem Ipsum.</p>

  <div class="abs service-card" style="left:160px">
    <div class="photo" role="img" aria-label="Photo of a hooded figure at a laptop in warm light" style="background:linear-gradient(135deg,#c88a3c,#6d4a25 60%,#2d241c)"></div>
    <div class="label">Offensive Security</div>
  </div>
  <div class="abs service-card" style="left:460px">
    <div class="photo" role="img" aria-label="Dark blue graphic with the words data protection above an open hand" style="background:radial-gradient(ellipse at 60% 40%,#3a5a8a,#12203a 70%)"></div>
    <div class="label">Data Protection Security</div>
  </div>
  <div class="abs service-card" style="left:761px">
    <div class="photo" role="img" aria-label="Phone showing a security alarm app beside a cutaway model house" style="background:linear-gradient(90deg,#d8d8d8,#f2f2f2 40%,#c9b9a6)"></div>
    <div class="label">Security Alarm</div>
  </div>
</section>

<section>
  <div class="abs consult" role="img" aria-label="Faded photo of people working in a modern office"></div>
  <div class="abs section-title consult-kicker cond">We Do</div>
  <div class="abs section-title consult-head">Security Consulting</div>
  <p class="abs consult-sub">Change how you work forever in seconds.</p>
  <div class="abs btn-ghost">CLICK HERE &#10148;</div>

  <div class="abs red-band">
    <h2>SPECIFICALLY OFFENSIVE SECURITY</h2>
    <p>Lorem Ipsum is simply dummy text of the printing</p>
  </div>
  <svg class="abs band-notch" width="60" height="18" viewBox="0 0 60 18"><polygon points="0,0 60,0 30,18" fill="#d51f27"/></svg>
</section>

<section>
  <div class="abs offer-photo" role="img" aria-label="Photo of two engineers with a laptop in a server room"></div>
  <div class="abs offer-panel">
    <div class="offer-kicker">OFFERINGS</div>
    <div class="offer-title">RED TEAM ADVERSARY SIMULATION</div>
    <p class="offer-copy">A goal based assessment where we attack just like a real world adversary. This includes external attacks and targeted phishing to demonstrate the real risk to your data.Internal Pivot Assessment &amp; Post Exploitation:We start as a low privileged users and attempted to move through the network in an attempt to access the data the matters to you. This is a simulation of a rogue trusted insider or a compromised internal host. We determine your risk when the egg shell is cracked. Even a seemingly insignificant compromise can have big consequences, and our goal is to demonstrate this risk.Advanced Product, Hardware &amp; RF Testing:This a highly customized assessment designed for you and your hardware. Depending on the product we will analyze custom RF protocols, reverse engineer OS and firmware, and analyze and fuzz network protocols. We have tested a range of products from toys to security products.</p>
    <span class="btn-outline">READ MORE &#10148;</span>
  </div>
</section>

<section>
  <div class="abs section-title clients-kicker">Clients That</div>
  <div class="abs section-title clients-title cond">Trust Us</div>
  <div class="abs testimonials" role="img" aria-label="Faded row of client portrait photos"></div>
  <div class="abs quote-card"></div>
  <div class="abs avatar" role="img" aria-label="Client portrait"></div>
  <div class="abs quote"><span class="quote-mark" style="position:absolute;left:-12px;top:-6px">&ldquo;</span>Lorem ipsum dolor sit amet, consectetur adipiscing elit. Donec dapibus odio vel tellus finibus placerat. In vel purus sed lacus sodales venenatis. Integer et convallis nulla, in fringilla nulla.<span class="quote-mark" style="position:absolute;right:-8px;top:30px">&rdquo;</span></div>
  <div class="abs quote-name">Martin Hale</div>
</section>

<section>
  <div class="abs section-title cond" style="top:2362px">Latest Blog</div>
  <div class="abs blog-rule"></div>

  <div class="abs blog-hero" role="img" aria-label="Photo of hands typing on a laptop in bright sunlight"></div>
  <div class="abs date" style="left:160px;top:2695px">15<small>DEC</small></div>

  <div class="abs post-thumb" role="img" aria-label="Photo of a padlock on a computer keyboard" style="top:2448px;background:linear-gradient(135deg,#555,#bfbfbf 50%,#c9a455)"></div>
  <div class="abs date" style="left:610px;top:2524px;width:44px">15<small>DEC</small></div>
  <div class="abs post-body" style="top:2448px">
    <h3>BLOG HEADING HERE</h3>
    <div class="post-meta">Posted By: <b>Joan Doe</b> on <b>April 5th,2017</b></div>
    <p class="post-excerpt">Lorem Ipsum is simply dummy text of the printing and typesetting industry. Lorem Ipsum has been the industry.</p>
    <div class="post-actions"><span class="btn-outline">READ MORE &#10148;</span>
      <span><svg width="11" height="10" viewBox="0 0 11 10"><path d="M1 1h9v6H4L1 9z" fill="#1d1d1d"/></svg>Comments</span>
      <span><svg width="11" height="10" viewBox="0 0 11 10"><path d="M5.5 9.5 1 5C-.5 3 1 0 3 .5c1 .2 2 1 2.5 2C6 1.5 7 .7 8 .5c2-.5 3.5 2.5 2 4.5z" fill="#1d1d1d"/></svg>0 Likes</span></div>
  </div>
  <div class="abs post-divider"></div>

  <div class="abs post-thumb" role="img" aria-label="Photo of a blue digital security interface" style="top:2621px;background:linear-gradient(135deg,#1d3c66,#4d87c2 50%,#a9c9e6)"></div>
  <div class="abs date" style="left:610px;top:2697px;width:44px">15<small>DEC</small></div>
  <div class="abs post-body" style="top:2621px">
    <h3>BLOG HEADING HERE</h3>
    <div class="post-meta">Posted By: <b>Joan Doe</b> on <b>April 5th,2017</b></div>
    <p class="post-excerpt">Lorem Ipsum is simply dummy text of the printing and typesetting industry. Lorem Ipsum has been the industry.</p>
    <div class="post-actions"><span class="btn-outline">READ MORE &#10148;</span>
      <span><svg width="11" height="10" viewBox="0 0 11 10"><path d="M1 1h9v6H4L1 9z" fill="#1d1d1d"/></svg>Comments</span>
      <span><svg width="11" height="10" viewBox="0 0 11 10"><path d="M5.5 9.5 1 5C-.5 3 1 0 3 .5c1 .2 2 1 2.5 2C6 1.5 7 .7 8 .5c2-.5 3.5 2.5 2 4.5z" fill="#1d1d1d"/></svg>0 Likes</span></div>
  </div>
</section>

<section>
  <div class="abs cta"></div>
  <div class="abs cta-title">SECURITY CONSULTING</div>
  <div class="abs cta-copy">Lorem Ipsum is simply dummy text of the printing and typesetting industry Lorem Ipsum.</div>
  <div class="abs btn-dark">GET FREE CONSULTATION <svg width="10" height="14" viewBox="0 0 10 14"><path d="M2 1l6 6-6 6" stroke="#fff" stroke-width="2.5" fill="none"/></svg></div>
</section>

<footer>
  <div class="abs footer"></div>
  <div class="abs newsletter">
    <h2>NEWSLETTER</h2>
    <p>Enter your email address for getting updates</p>
    <div class="subscribe"><div class="field">Enter your email id</div><div class="go">Subscribe</div></div>
  </div>
  <div class="abs join">Join the conversation</div>
  <div class="abs socials"><span></span><span></span><span></span><span></span><span></span></div>
  <div class="abs footer-links">HOME<i>|</i>ABOUT US<i>|</i>OUR SERVICES<i>|</i>CONTACT US</div>
  <div class="abs copyright">Blue Harbor © 2017 All rights reserved</div>
</footer>

</body>
</html>
```